Need a business letterhead for word docs

Hi, I need a business letterhead. We have had some before but they have issues printing them. I have attached a sample of what we have used that I want improved :) and a PSD of our logo, please use the one with all caps. This will be used for all our correspondance with clients and profeesionals. Our client base are children, so these documents will go to their parents and doctors and paediatricians who also treat these children.

Target Market(s)

Clients (who are families and children) and doctors/paediatricians

Industry/Entity Type

Health Care

Font styles to use
Sans Serif

Colors
85cae6

Requirements
Must have
• My logo and the feel of my logo
Nice to have
• clean feel

```html
<!DOCTYPE html>
<html lang="en">
<head>
<meta charset="utf-8">
<title>Little Sprout Letterhead</title>
<link rel="stylesheet" href="https://fonts.googleapis.com/css2?family=Roboto+Slab:wght@400;700&display=swap">
<style>
  :root {
    --paper: #ffffff;
    --ink: #1b1b1b;
    --label-blue: #1a73c5;
    --brand-sky: #2fb4e9;
    --tagline-blue: #1a6fbf;
  }
  * { margin: 0; padding: 0; box-sizing: border-box; }
  html, body {
    width: 923px;
    height: 1200px;
    overflow: hidden;
    background: var(--paper);
  }
  .letterhead {
    position: relative;
    width: 923px;
    height: 1200px;
    background: var(--paper);
    font-family: "Roboto Slab", serif;
    color: var(--ink);
  }
  .contact {
    position: absolute;
    left: 21px;
    top: 36px;
    font-size: 14.5px;
    line-height: 20px;
  }
  .contact-label {
    color: var(--label-blue);
    font-weight: 700;
  }
  .contact-indent { padding-left: 22px; }
  .contact-gap { height: 20px; }
  .contact-spacer { display: inline-block; width: 14px; }
  .brand {
    position: absolute;
    right: 22px;
    top: 108px;
    display: flex;
    align-items: center;
    gap: 10px;
  }
  .brand-dot {
    width: 18px;
    height: 18px;
    border-radius: 50%;
    background: var(--brand-sky);
  }
  .brand-name {
    font-family: "Roboto Slab", serif;
    font-weight: 700;
    font-size: 25px;
    letter-spacing: 0.5px;
    color: var(--brand-sky);
  }
  .tagline {
    position: absolute;
    left: 0;
    right: 0;
    top: 1150px;
    text-align: center;
    font-size: 24px;
    font-weight: 700;
    color: var(--tagline-blue);
  }
</style>
</head>
<body>
  <main class="letterhead">
    <address class="contact" style="font-style: normal;">
      <div><span class="contact-label">A:</span> 8 Larkfield Lane, Elwood 3184</div>
      <div class="contact-indent">41 Tamsin Road, Hampton 3188</div>
      <div class="contact-gap"></div>
      <div><span class="contact-label">P:</span> 03 9000 4127<span class="contact-spacer"></span><span class="contact-label">E:</span> hello@littlesproutclinic.com.au</div>
      <div><span class="contact-label">W:</span> www.littlesproutclinic.com.au</div>
    </address>

    <div class="brand">
      <span class="brand-dot"></span>
      <span class="brand-name">LITTLE SPROUT</span>
    </div>

    <p class="tagline">Room to Grow for Every Child</p>
  </main>
</body>
</html>
```